We require a business card that promotes our Electrical business. Things we would like included are;
1) our business name, Bright Path Electrical and Communication
2) Our Electrical licence, EC 27036
3) Our ABN, 52 147 906 318
4) Our website, www.ridgewirecrew.com.au
5) Our Email, info@ridgewirecrew.com.au
6) Our contact number, 0452 681 207
7) Our address, 48 Marlow Rd Tandridge Perth 6093
8) Our logo, I will attach this (can you please change it so the ackground is white not black)
9) Our colours are red and white and perhaps some black
10) Managing Director Dorian Velcourt
11) the back to say 'notes' and have some lines for writing

Target Market(s)

General

Industry/Entity Type

Electrical

Contact Information for Business Card

Include the colour white, black and red.

Font styles to use
Sans Serif

Requirements
Nice to have
• A thunder bolt or a power point or a cord or something electrical, cartoon image of a cartoon like electrical tradie

```html
<!DOCTYPE html>
<html lang="en">
<head>
<meta charset="utf-8">
<title>Bright Path Electrical and Communication – Business Card</title>
<link rel="stylesheet" href="https://fonts.googleapis.com/css2?family=Didact+Gothic&display=swap">
<style>
  :root {
    --ink: #111111;
    --paper: #ffffff;
    --signal-red: #e01f26;
    --rule-grey: #b9b9b9;
    --stage: #ecebe8;
    --muted-white: #f4f4f4;
  }
  * { box-sizing: border-box; margin: 0; padding: 0; }
  html, body {
    width: 1200px; height: 900px; overflow: hidden;
    background: var(--stage);
    font-family: "Didact Gothic", "Century Gothic", sans-serif;
  }
  .card-set {
    position: absolute; inset: 0;
    display: flex; align-items: center; justify-content: center; gap: 40px;
  }
  .card {
    position: relative; width: 540px; height: 330px; overflow: hidden;
    box-shadow: 0 6px 18px rgba(0,0,0,.18);
  }
  .card--front { background: var(--ink); color: var(--muted-white); }
  .card--back { background: var(--paper); color: var(--ink); }

  .brand { position: absolute; line-height: 1; }
  .brand__name { font-size: 40px; letter-spacing: .5px; display: flex; align-items: center; gap: 10px; }
  .brand__mark { width: 14px; height: 14px; border-radius: 50%; background: var(--signal-red); }
  .brand__line { font-size: 12.5px; text-transform: uppercase; letter-spacing: .4px; margin-top: 4px; }
  .card--front .brand { left: 34px; top: 34px; color: var(--muted-white); }
  .card--back .brand { left: 50%; top: 62px; transform: translateX(-50%); color: var(--ink); text-align: left; }

  .contact-list { position: absolute; left: 40px; top: 118px; list-style: none; font-size: 15px; line-height: 20px; }
  .contact-list li { display: flex; align-items: center; gap: 9px; }
  .contact-list svg { width: 12px; height: 12px; flex: none; }
  .address { position: absolute; left: 40px; top: 188px; font-size: 15px; line-height: 20px; }

  .person { position: absolute; right: 44px; top: 128px; text-align: right; font-size: 16px; line-height: 21px; }
  .person__name { color: var(--signal-red); letter-spacing: .5px; }
  .person__role { color: var(--muted-white); }

  .credentials { position: absolute; right: 54px; top: 232px; font-size: 15px; line-height: 19px; }

  .decor { position: absolute; inset: 0; width: 100%; height: 100%; }

  .note-lines { position: absolute; left: 46px; right: 46px; top: 160px; }
  .note-lines span { display: block; height: 1px; background: var(--rule-grey); margin-bottom: 38px; }
</style>
</head>
<body>
<main class="card-set">

  <section class="card card--front" aria-label="Business card front">
    <svg class="decor" viewBox="0 0 540 330" aria-hidden="true">
      <polygon points="0,262 152,262 142,290 0,290" fill="var(--paper)"/>
      <polygon points="160,262 148,296 0,296 0,330 540,330 540,304" fill="var(--signal-red)"/>
      <polygon points="498,150 510,150 514,192 494,192" fill="var(--paper)"/>
      <polygon points="516,150 540,150 540,192 520,192" fill="var(--signal-red)"/>
    </svg>

    <div class="brand">
      <div class="brand__name">Bright Path <span class="brand__mark"></span></div>
      <div class="brand__line">Electrical and Communication</div>
    </div>

    <ul class="contact-list">
      <li>
        <svg viewBox="0 0 12 12"><circle cx="6" cy="6" r="5.5" fill="var(--signal-red)"/><path d="M1 6h10M6 1c2.5 2.8 2.5 7.2 0 10M6 1c-2.5 2.8-2.5 7.2 0 10" stroke="var(--ink)" stroke-width=".9" fill="none"/></svg>
        www.ridgewirecrew.com.au
      </li>
      <li>
        <svg viewBox="0 0 12 12"><rect x="0.5" y="2" width="11" height="8" fill="var(--signal-red)"/><path d="M1 2.5l5 4 5-4" stroke="var(--ink)" stroke-width="1" fill="none"/></svg>
        info@ridgewirecrew.com.au
      </li>
      <li>
        <svg viewBox="0 0 12 12"><rect x="2.5" y="0.5" width="7" height="11" rx="1.2" fill="none" stroke="var(--signal-red)" stroke-width="1.3"/><circle cx="6" cy="9.3" r=".8" fill="var(--signal-red)"/></svg>
        0452 681 207
      </li>
    </ul>

    <p class="address">48 Marlow Rd Tandridge<br>Perth 6093</p>

    <div class="person">
      <div class="person__name">Dorian Velcourt</div>
      <div class="person__role">Managing Director</div>
    </div>

    <p class="credentials">Electrical licence,<br>EC 27036 ABN,<br>52 147 906 318</p>
  </section>

  <section class="card card--back" aria-label="Business card back">
    <div class="brand">
      <div class="brand__name">Bright Path <span class="brand__mark"></span></div>
      <div class="brand__line">Electrical and Communication</div>
    </div>
    <div class="note-lines" aria-hidden="true">
      <span></span><span></span><span></span>
    </div>
  </section>

</main>
</body>
</html>
```